Medical Flight Brochure

We are a medical flight company in need of a new brochure targeting nurse case managers who work at hospitals. Our service provides paramedic and nurses to fly with sick people on commercial flights anywhere in the world. We want the case managers to understand that we are a better and less expensive service than they typically use. Attached you will find the copy for the brochure as well as some text that we would like turned into a chart for use in the brochure as well. A tri-fold brochure is preferred. Thanks so much!
Updates

In the brochure copy that we attached, we included information that we wanted to be represented in a chart in the brochure. We were not clear about this, so we are now attaching a sample chart as an example of what we want in the brochure. Please don't use this exact chart, but instead create one like it (with the same information) that looks nice as part of the brochure. Thanks everyone for the hard work!

Reason: We have had a number of excellent submissions. Our team is traveling and may not be very fast at providing feedback, so we are extending the deadline by 5 days. Thank you everyone for the hard work!

Target Market(s)

Hospital nurse case managers

Industry/Entity Type

Medical

Requirements
Should not have
• Cartoons or childish elements

```html
<!DOCTYPE html>
<html lang="en">
<head>
<meta charset="utf-8">
<title>CareWing Services – Tri-fold Brochure</title>
<link rel="stylesheet" href="https://fonts.googleapis.com/css2?family=Arimo:wght@400;700&display=swap">
<style>
  :root {
    --blue: #1a8ad8;
    --blue-deep: #1467b8;
    --blue-soft: #8fb6e6;
    --blue-pale: #dbe8f6;
    --ink: #2b2b2b;
    --grey: #8a8a8a;
    --panel-light: #f1f1f1;
    --photo-top: #b7c6d3;
    --photo-bottom: #8e979e;
    --backdrop: #a9a9a9;
    --white: #ffffff;
  }
  * { box-sizing: border-box; margin: 0; padding: 0; }
  html, body { width: 1200px; height: 1038px; overflow: hidden; }
  body { background: var(--backdrop); font-family: "Arimo", Arial, sans-serif; position: relative; }

  .brochure {
    position: absolute; left: 50px; top: 94px; width: 1100px; height: 850px;
    background: var(--white); box-shadow: 0 10px 30px rgba(0,0,0,.25); overflow: hidden;
  }
  .panel { position: absolute; top: 0; height: 850px; width: 367px; }
  .panel--chart { left: 0; background: var(--white); }
  .panel--back { left: 367px; background: var(--blue); }
  .panel--cover { left: 734px; width: 366px; background: linear-gradient(180deg, #f6f6f6, var(--panel-light)); }

  /* Chart panel */
  .chart-corner { position: absolute; left: 0; top: 0; }
  .chart-title {
    position: absolute; left: 0; top: 212px; width: 367px; height: 60px;
    background: rgba(255,255,255,.88); font-weight: 700; font-size: 21px; color: var(--ink);
    text-align: center; line-height: 60px;
  }
  .legend { position: absolute; left: 70px; top: 300px; list-style: none; }
  .legend li { display: flex; align-items: center; gap: 10px; font-size: 18px; color: var(--ink); margin-bottom: 14px; }
  .swatch { width: 20px; height: 20px; display: inline-block; flex: none; }
  .swatch--blue { background: var(--blue); }
  .swatch--grey { background: var(--grey); }
  .bar-chart { position: absolute; left: 60px; }
  .bar-chart--domestic { top: 390px; }
  .bar-chart--international { top: 545px; }
  .chart-strip { position: absolute; left: 0; bottom: 0; width: 367px; height: 26px; background: var(--blue); }

  /* Brand lines */
  .brand { position: absolute; left: 0; display: flex; align-items: center; justify-content: center; gap: 12px; font-weight: 700; font-size: 26px; white-space: nowrap; }
  .brand-dot { width: 40px; height: 40px; border-radius: 50%; flex: none; }
  .brand--back { width: 367px; top: 72px; color: var(--white); }
  .brand--back .brand-dot { background: var(--white); }
  .brand--cover { width: 366px; top: 78px; color: #3c3c3c; }
  .brand--cover .brand-dot { background: var(--blue); }

  /* Photo area */
  .photo {
    position: absolute; left: 367px; top: 175px; width: 668px; height: 510px;
    background: linear-gradient(180deg, var(--photo-top), var(--photo-bottom));
  }
  .photo-underline { position: absolute; left: 367px; top: 685px; width: 367px; height: 16px; background: var(--blue-deep); }
  .back-web { position: absolute; left: 0; top: 735px; width: 367px; text-align: center; color: var(--white); font-size: 17px; }

  /* Cover panel */
  .cover-frame { position: absolute; left: 734px; top: 0; }
  .contact { position: absolute; right: 40px; top: 712px; text-align: right; font-size: 14px; font-style: normal; color: var(--ink); line-height: 1.6; }
  .cover-strip { position: absolute; left: 0; bottom: 32px; width: 366px; height: 22px; background: var(--blue); }
</style>
</head>
<body>
  <main class="brochure">
    <section class="panel panel--chart">
      <svg class="chart-corner" width="367" height="280" viewBox="0 0 367 280">
        <polygon points="0,0 230,0 90,212 0,212" fill="var(--blue)"/>
        <polygon points="210,0 280,0 140,212 70,212" fill="var(--blue-deep)" opacity=".55"/>
        <polygon points="280,0 367,0 367,110 240,212 140,212" fill="var(--blue-pale)"/>
      </svg>
      <h2 class="chart-title">Average Trip Cost</h2>
      <ul class="legend">
        <li><span class="swatch swatch--blue"></span>Air Ambulance</li>
        <li><span class="swatch swatch--grey"></span>CareWing Services</li>
      </ul>

      <svg class="bar-chart bar-chart--domestic" width="250" height="140" viewBox="0 0 250 140">
        <defs>
          <linearGradient id="boxGrad" x1="0" y1="0" x2="1" y2="0">
            <stop offset="0" stop-color="#a8a8a8"/><stop offset=".5" stop-color="#e6e6e6"/><stop offset="1" stop-color="#a8a8a8"/>
          </linearGradient>
        </defs>
        <rect x="0" y="0" width="250" height="116" fill="url(#boxGrad)"/>
        <rect x="40" y="44" width="70" height="68" fill="var(--blue)"/>
        <rect x="135" y="91" width="70" height="21" fill="var(--grey)"/>
        <line x1="10" y1="112" x2="240" y2="112" stroke="#222" stroke-width="2"/>
        <text x="75" y="36" text-anchor="middle" font-size="15" fill="#222" font-family="Arimo, sans-serif">$23,800</text>
        <text x="170" y="83" text-anchor="middle" font-size="15" fill="#222" font-family="Arimo, sans-serif">$7,400</text>
        <text x="125" y="134" text-anchor="middle" font-size="15" font-weight="700" fill="#111" font-family="Arimo, sans-serif">Domestic</text>
      </svg>

      <svg class="bar-chart bar-chart--international" width="250" height="270" viewBox="0 0 250 270">
        <rect x="0" y="0" width="250" height="245" fill="url(#boxGrad)"/>
        <rect x="40" y="55" width="70" height="186" fill="var(--blue)"/>
        <rect x="135" y="179" width="70" height="62" fill="var(--grey)"/>
        <line x1="10" y1="241" x2="240" y2="241" stroke="#222" stroke-width="2"/>
        <text x="75" y="46" text-anchor="middle" font-size="15" fill="#222" font-family="Arimo, sans-serif">$78,900</text>
        <text x="170" y="170" text-anchor="middle" font-size="15" fill="#222" font-family="Arimo, sans-serif">$26,200</text>
        <text x="125" y="263" text-anchor="middle" font-size="15" font-weight="700" fill="#111" font-family="Arimo, sans-serif">International</text>
      </svg>
      <div class="chart-strip"></div>
    </section>

    <section class="panel panel--back">
      <div class="brand brand--back"><span class="brand-dot"></span>CareWing Services</div>
      <p class="back-web">www.carewingservices.com</p>
    </section>

    <section class="panel panel--cover">
      <div class="brand brand--cover"><span class="brand-dot"></span>CareWing Services</div>
      <address class="contact">1-888-555-0147<br>www.carewingservices.com</address>
      <div class="cover-strip"></div>
    </section>

    <div class="photo" role="img" aria-label="Photo: passenger jet taking off from a runway"></div>
    <div class="photo-underline"></div>

    <svg class="cover-frame" width="366" height="700" viewBox="0 0 366 700">
      <polygon points="150,175 366,205 366,232 270,218" fill="var(--blue-deep)" opacity=".75"/>
      <polygon points="290,220 330,226 260,685 220,685" fill="var(--blue)" opacity=".6"/>
      <polygon points="330,226 366,232 366,300 300,685 260,685" fill="var(--blue-soft)" opacity=".6"/>
    </svg>
  </main>
</body>
</html>
```